Web Button design and production

I need remote control like buttons (or your own design of buttons if I like it)
3x4 text buttons (normal, pressed, disabled)
3x1 empty button (normal, pressed, disabled)
3x6 buttons with glyph (normal, pressed, disabled)
3x288 with 24h time "00:00", "00:05", "00:10" (normal, pressed, disabled)
4 LED (red, green, orange, black)
I will upload the background image as soon as possible (black plastic)
See attached images
Q: Do the buttons have to be gray/black?
A: It should look like a high end remote control. It could be brushed aluminum as well, or something you come up with. But I guess black or dark grey would be best. The background will be picsharbor 40561739, but it's not available yet.
Q: Do I have to provide all buttons for the contest?
A: No! I only need one button (3 states) and a LED to decide. Only the winner will do the whole job.
Q: Is the Designer who wins the contest expected to complete all the extra buttons?
A: Yes, please.
Plastic

```html
<!DOCTYPE html>
<html lang="en">
<head>
<meta charset="utf-8">
<title>Remote Control Button Set</title>
<link rel="stylesheet" href="https://fonts.googleapis.com/css2?family=Questrial&display=swap">
<style>
  :root{
    --bg:#1b1b1b;
    --bg-edge:#111;
    --btn-top:#2e2e2e;
    --btn-bottom:#070707;
    --rim:#a9a9a9;
    --rim-dark:#4a4a4a;
    --label:#f2f2f2;
    --label-active:#2f9fe6;
    --label-off:#3a3a3a;
    --rim-off:#4c4c4c;
    --led-red:#e0241c;
    --led-green:#7cc234;
    --led-orange:#f1c11a;
  }
  *{box-sizing:border-box;margin:0;padding:0}
  html,body{width:1200px;height:1200px;overflow:hidden}
  body{
    background:radial-gradient(ellipse at 50% 40%, #262626 0%, var(--bg) 55%, var(--bg-edge) 100%);
    font-family:"Questrial", "Century Gothic", sans-serif;
    position:relative;
  }
  .glyph-defs{position:absolute;width:0;height:0}
  .state{
    position:absolute;left:223px;
    display:flex;gap:53px;
  }
  .state--normal{top:56px}
  .state--pressed{top:438px}
  .state--disabled{top:810px}

  .left-block{
    display:grid;
    grid-template-columns:117px 179px;
    grid-template-rows:117px 50px 112px;
    column-gap:28px;row-gap:15px;
  }
  .led-row{
    grid-column:1 / span 2;
    display:flex;justify-content:space-between;align-items:center;
    padding:0 4px;
  }
  .key-grid{
    display:grid;
    grid-template-columns:repeat(3,118px);
    grid-auto-rows:62px;
    column-gap:26px;row-gap:22px;
    margin-left:-2px;
  }

  .key{
    position:relative;
    display:flex;align-items:center;justify-content:center;
    border-radius:13px;
    border:3px solid var(--rim);
    background:linear-gradient(180deg,var(--btn-top) 0%,#161616 50%,var(--btn-bottom) 51%,#141414 100%);
    box-shadow:0 0 0 2px #0a0a0a, 0 0 0 3px var(--rim-dark), inset 0 0 0 2px #000, inset 0 3px 6px rgba(255,255,255,.12), 0 6px 10px rgba(0,0,0,.6);
    color:var(--label);
    font-size:25px;line-height:1.05;text-align:center;text-transform:uppercase;
    letter-spacing:.5px;
  }
  .key svg{width:34px;height:34px;fill:currentColor}
  .key--square svg{width:28px;height:28px}
  .key--time{font-size:26px}
  .led{
    width:46px;height:40px;border-radius:7px;
    border:2px solid var(--rim);
    background:linear-gradient(180deg,#2a2a2a,#060606);
    box-shadow:0 0 0 2px #0a0a0a, inset 0 0 0 1px #000;
    display:flex;align-items:center;justify-content:center;
  }
  .led svg{width:28px;height:24px;fill:none;stroke:currentColor;stroke-width:2.6;stroke-linecap:round}
  .led--black{color:#f2f2f2}
  .led--red{color:var(--led-red)}
  .led--green{color:var(--led-green)}
  .led--orange{color:var(--led-orange)}
  .state--pressed .led--black{color:var(--label-active)}

  .state--pressed .key{
    color:var(--label-active);
    background:linear-gradient(180deg,#0c0c0c 0%,#151515 50%,#1d1d1d 100%);
    box-shadow:0 0 0 2px #0a0a0a, 0 0 0 3px var(--rim-dark), inset 0 3px 8px rgba(0,0,0,.9), 0 4px 8px rgba(0,0,0,.5);
  }
  .state--disabled .key,
  .state--disabled .led{
    color:var(--label-off);
    border-color:var(--rim-off);
    background:linear-gradient(180deg,#1f1f1f,#151515);
    box-shadow:0 0 0 2px #0e0e0e, 0 0 0 3px #2c2c2c;
  }
  .state--disabled .led{width:40px;height:34px}
  .state--disabled .led svg{display:none}
</style>
</head>
<body>
<svg class="glyph-defs" aria-hidden="true">
  <symbol id="g-play" viewBox="0 0 24 24"><path d="M8 5l9 7-9 7z"/></symbol>
  <symbol id="g-back" viewBox="0 0 24 24"><path d="M16 5l-9 7 9 7z"/></symbol>
  <symbol id="g-next" viewBox="0 0 24 24"><path d="M5 4l11 8-11 8z"/><rect x="17" y="4" width="3.5" height="16"/></symbol>
  <symbol id="g-prev" viewBox="0 0 24 24"><rect x="3.5" y="4" width="3.5" height="16"/><path d="M19 4L8 12l11 8z"/></symbol>
  <symbol id="g-left" viewBox="0 0 24 24"><path d="M2 12l9-8v5h11v6H11v5z"/></symbol>
  <symbol id="g-return" viewBox="0 0 24 24"><path d="M2 17l7-7v4h6a2 2 0 0 0 2-2V4h5v9a6 6 0 0 1-6 6H9v4z"/></symbol>
  <symbol id="g-signal" viewBox="0 0 28 24"><path d="M4 10a14 14 0 0 1 20 0"/><path d="M8 14a8 8 0 0 1 12 0"/><path d="M11.5 17.5a3.4 3.4 0 0 1 5 0"/><circle cx="14" cy="21" r="1.2" fill="currentColor"/></symbol>
</svg>

<section class="state state--normal" aria-label="Normal state">
  <div class="left-block">
    <div class="key key--square"><svg><use href="#g-play"/></svg></div>
    <div class="key">Jetzt<br>Buchen</div>
    <div class="led-row">
      <span class="led led--black"><svg><use href="#g-signal"/></svg></span>
      <span class="led led--red"><svg><use href="#g-signal"/></svg></span>
      <span class="led led--green"><svg><use href="#g-signal"/></svg></span>
      <span class="led led--orange"><svg><use href="#g-signal"/></svg></span>
    </div>
    <div class="key key--square"><svg><use href="#g-back"/></svg></div>
    <div class="key">Book<br>Now</div>
  </div>
  <div class="key-grid">
    <div class="key"><svg><use href="#g-next"/></svg></div>
    <div class="key"></div>
    <div class="key">Login</div>
    <div class="key"><svg><use href="#g-prev"/></svg></div>
    <div class="key key--time">01:25</div>
    <div class="key key--time">18:25</div>
    <div class="key"><svg><use href="#g-left"/></svg></div>
    <div class="key key--time">02:25</div>
    <div class="key key--time">18:25</div>
    <div class="key"><svg><use href="#g-return"/></svg></div>
    <div class="key key--time">03:25</div>
    <div class="key key--time">18:25</div>
  </div>
</section>

<section class="state state--pressed" aria-label="Pressed state">
  <div class="left-block">
    <div class="key key--square"><svg><use href="#g-play"/></svg></div>
    <div class="key">Jetzt<br>Buchen</div>
    <div class="led-row">
      <span class="led led--black"><svg><use href="#g-signal"/></svg></span>
      <span class="led led--red"><svg><use href="#g-signal"/></svg></span>
      <span class="led led--green"><svg><use href="#g-signal"/></svg></span>
      <span class="led led--orange"><svg><use href="#g-signal"/></svg></span>
    </div>
    <div class="key key--square"><svg><use href="#g-back"/></svg></div>
    <div class="key">Book<br>Now</div>
  </div>
  <div class="key-grid">
    <div class="key"><svg><use href="#g-next"/></svg></div>
    <div class="key"></div>
    <div class="key">Login</div>
    <div class="key"><svg><use href="#g-prev"/></svg></div>
    <div class="key key--time">01:25</div>
    <div class="key key--time">18:25</div>
    <div class="key"><svg><use href="#g-left"/></svg></div>
    <div class="key key--time">02:25</div>
    <div class="key key--time">18:25</div>
    <div class="key"><svg><use href="#g-return"/></svg></div>
    <div class="key key--time">03:25</div>
    <div class="key key--time">18:25</div>
  </div>
</section>

<section class="state state--disabled" aria-label="Disabled state">
  <div class="left-block">
    <div class="key key--square"><svg><use href="#g-play"/></svg></div>
    <div class="key">Jetzt<br>Buchen</div>
    <div class="led-row">
      <span class="led"><svg><use href="#g-signal"/></svg></span>
      <span class="led"><svg><use href="#g-signal"/></svg></span>
      <span class="led"><svg><use href="#g-signal"/></svg></span>
      <span class="led"><svg><use href="#g-signal"/></svg></span>
    </div>
    <div class="key key--square"><svg><use href="#g-back"/></svg></div>
    <div class="key">Book<br>Now</div>
  </div>
  <div class="key-grid">
    <div class="key"><svg><use href="#g-next"/></svg></div>
    <div class="key"></div>
    <div class="key">Login</div>
    <div class="key"><svg><use href="#g-prev"/></svg></div>
    <div class="key key--time">01:25</div>
    <div class="key key--time">18:25</div>
    <div class="key"><svg><use href="#g-left"/></svg></div>
    <div class="key key--time">02:25</div>
    <div class="key key--time">18:25</div>
    <div class="key"><svg><use href="#g-return"/></svg></div>
    <div class="key key--time">03:25</div>
    <div class="key key--time">18:25</div>
  </div>
</section>
</body>
</html>
```